Velmar Ops Business Cards

We need to design some upbeat business cards. We are an Industrial Rope Access Company/Height Safety Company that specialize in Rope Access, Confined Space, Anchor Points, Safety Systems, PPE Inspecions and Rigging.
Company name is Velmar Ops Ltd
Card is for Gareth Lomas the Company Director
His mobile number is 027 418 9072 and email is gareth@velmarops.co.nz. Website address is www.velmarops.co.nz.
We will post some pictures below to ensure you get a good idea of what we do.

```html
<!DOCTYPE html>
<html lang="en">
<head>
<meta charset="utf-8">
<title>Velmar Ops Business Cards</title>
<link href="https://fonts.googleapis.com/css2?family=Saira:wght@600;700&family=Open+Sans:wght@300;400&display=swap" rel="stylesheet">
<style>
  :root {
    --backdrop: #1e1e20;
    --card: #0c0c0d;
    --card-edge: #232326;
    --blue: #2350b8;
    --white: #ffffff;
    --muted: #c9c9cc;
  }
  * { box-sizing: border-box; margin: 0; padding: 0; }
  html, body { width: 1200px; height: 896px; overflow: hidden; }
  body {
    background: var(--backdrop);
    position: relative;
    font-family: "Saira", sans-serif;
  }
  .card {
    position: absolute;
    top: 296px;
    width: 530px;
    height: 303px;
    border-radius: 16px;
    background: linear-gradient(150deg, #19191b 0%, var(--card) 55%, #050505 100%);
    border: 1px solid var(--card-edge);
    overflow: hidden;
    color: var(--white);
  }
  .card--services { left: 40px; }
  .card--contact { left: 630px; }

  /* Services side */
  .services-band {
    position: absolute;
    left: 0; right: 0;
    top: 124px;
    height: 52px;
    background: var(--blue);
    display: flex;
    align-items: center;
    justify-content: center;
    font-weight: 700;
    font-size: 34px;
    letter-spacing: 1px;
  }
  .service-list {
    position: absolute;
    list-style: none;
    font-weight: 600;
    font-size: 15px;
    line-height: 17px;
  }
  .service-list li { display: flex; align-items: center; gap: 8px; }
  .service-list--upper { top: 14px; right: 26px; }
  .service-list--upper li { justify-content: flex-end; }
  .service-list--lower { top: 184px; left: 26px; }
  .tick { width: 12px; height: 12px; flex: none; }

  /* Contact side */
  .brand-band {
    position: absolute;
    left: 0; top: 38px;
    width: 330px; height: 72px;
  }
  .brand-band svg { position: absolute; inset: 0; }
  .brand-name {
    position: absolute;
    left: 28px; top: 0; height: 72px;
    display: flex; align-items: center;
    font-weight: 700;
    font-size: 44px;
    letter-spacing: 1px;
  }
  .person {
    position: absolute;
    right: 232px; top: 206px;
    text-align: right;
    font-family: "Open Sans", sans-serif;
  }
  .person-name { font-size: 21px; font-weight: 400; line-height: 24px; }
  .person-role { font-size: 13px; font-weight: 300; color: var(--muted); }
  .divider {
    position: absolute;
    left: 310px; top: 196px;
    width: 1px; height: 56px;
    background: var(--muted);
  }
  .contact-list {
    position: absolute;
    left: 322px; top: 196px;
    list-style: none;
    font-family: "Open Sans", sans-serif;
    font-weight: 300;
    font-size: 12.5px;
    line-height: 19px;
  }
  .contact-list li { display: flex; align-items: center; gap: 6px; }
  .contact-icon { width: 10px; height: 10px; flex: none; }
</style>
</head>
<body>

<section class="card card--services" aria-label="Card back: services">
  <ul class="service-list service-list--upper">
    <li>Confined Space<svg class="tick" viewBox="0 0 12 12"><rect x="0.5" y="0.5" width="11" height="11" fill="none" stroke="#2350b8"/><path d="M3 6l2 2 5-6" fill="none" stroke="#2350b8" stroke-width="1.4"/></svg></li>
    <li>Safety Systems<svg class="tick" viewBox="0 0 12 12"><rect x="0.5" y="0.5" width="11" height="11" fill="none" stroke="#2350b8"/><path d="M3 6l2 2 5-6" fill="none" stroke="#2350b8" stroke-width="1.4"/></svg></li>
    <li>Rigging<svg class="tick" viewBox="0 0 12 12"><rect x="0.5" y="0.5" width="11" height="11" fill="none" stroke="#2350b8"/><path d="M3 6l2 2 5-6" fill="none" stroke="#2350b8" stroke-width="1.4"/></svg></li>
    <li>Confined Space<svg class="tick" viewBox="0 0 12 12"><rect x="0.5" y="0.5" width="11" height="11" fill="none" stroke="#2350b8"/><path d="M3 6l2 2 5-6" fill="none" stroke="#2350b8" stroke-width="1.4"/></svg></li>
    <li>Safety Systems<svg class="tick" viewBox="0 0 12 12"><rect x="0.5" y="0.5" width="11" height="11" fill="none" stroke="#2350b8"/><path d="M3 6l2 2 5-6" fill="none" stroke="#2350b8" stroke-width="1.4"/></svg></li>
    <li>Rigging<svg class="tick" viewBox="0 0 12 12"><rect x="0.5" y="0.5" width="11" height="11" fill="none" stroke="#2350b8"/><path d="M3 6l2 2 5-6" fill="none" stroke="#2350b8" stroke-width="1.4"/></svg></li>
  </ul>

  <div class="services-band">www.velmarops.co.nz</div>

  <ul class="service-list service-list--lower">
    <li><svg class="tick" viewBox="0 0 12 12"><rect x="0.5" y="0.5" width="11" height="11" fill="none" stroke="#2350b8"/><path d="M3 6l2 2 5-6" fill="none" stroke="#2350b8" stroke-width="1.4"/></svg>Rope Access</li>
    <li><svg class="tick" viewBox="0 0 12 12"><rect x="0.5" y="0.5" width="11" height="11" fill="none" stroke="#2350b8"/><path d="M3 6l2 2 5-6" fill="none" stroke="#2350b8" stroke-width="1.4"/></svg>Anchor Points</li>
    <li><svg class="tick" viewBox="0 0 12 12"><rect x="0.5" y="0.5" width="11" height="11" fill="none" stroke="#2350b8"/><path d="M3 6l2 2 5-6" fill="none" stroke="#2350b8" stroke-width="1.4"/></svg>PPE Certification</li>
    <li><svg class="tick" viewBox="0 0 12 12"><rect x="0.5" y="0.5" width="11" height="11" fill="none" stroke="#2350b8"/><path d="M3 6l2 2 5-6" fill="none" stroke="#2350b8" stroke-width="1.4"/></svg>Rope Access</li>
    <li><svg class="tick" viewBox="0 0 12 12"><rect x="0.5" y="0.5" width="11" height="11" fill="none" stroke="#2350b8"/><path d="M3 6l2 2 5-6" fill="none" stroke="#2350b8" stroke-width="1.4"/></svg>Anchor Points</li>
    <li><svg class="tick" viewBox="0 0 12 12"><rect x="0.5" y="0.5" width="11" height="11" fill="none" stroke="#2350b8"/><path d="M3 6l2 2 5-6" fill="none" stroke="#2350b8" stroke-width="1.4"/></svg>PPE Certification</li>
  </ul>
</section>

<section class="card card--contact" aria-label="Card front: contact details">
  <div class="brand-band">
    <svg viewBox="0 0 330 72" width="330" height="72" aria-hidden="true">
      <polygon points="0,0 330,0 282,72 0,72" fill="#2350b8"/>
    </svg>
    <div class="brand-name">Velmar Ops</div>
  </div>

  <div class="person">
    <div class="person-name">Gareth Lomas</div>
    <div class="person-role">Director</div>
  </div>

  <div class="divider"></div>

  <ul class="contact-list">
    <li><svg class="contact-icon" viewBox="0 0 10 10"><rect x="2" y="0.5" width="6" height="9" rx="1" fill="none" stroke="#fff"/></svg>: 027 418 9072</li>
    <li><svg class="contact-icon" viewBox="0 0 10 10"><rect x="0.5" y="2" width="9" height="6" fill="none" stroke="#fff"/><path d="M0.5 2l4.5 3.5 4.5-3.5" fill="none" stroke="#fff"/></svg>: gareth@velmarops.co.nz</li>
    <li><svg class="contact-icon" viewBox="0 0 10 10"><circle cx="5" cy="5" r="4.5" fill="#fff"/><path d="M0.5 5h9M5 0.5v9" stroke="#0c0c0d" stroke-width="0.8"/></svg>: www.velmarops.co.nz</li>
  </ul>
</section>

</body>
</html>
```